Single brochure for international companies in the financial sector

We need to update a brochure 4 pages presenting our company. We are a financial engineering company. The final design must provide financial security, service and trust. you will find the current brochure copy. Our color code is Orange (RGB 235/100/68), Black, White and Gray. photos show the visual of the site, but it is not mandatory to keep them.

Target Market(s)

wealth management professionals

Industry/Entity Type

Finance

Requirements
Must have
• Logo Velbrook Capital all text in the document color Orange Velbrook (RGB 235/100/68)
Nice to have
• Vista Font
Should not have
• images / pictures of people

```html
<!DOCTYPE html>
<html lang="en">
<head>
<meta charset="utf-8">
<title>Velbrook Capital – Brochure</title>
<link rel="stylesheet" href="https://fonts.googleapis.com/css2?family=Questrial&display=swap">
<style>
  :root{
    --orange:#eb6444;
    --black:#1e1e1e;
    --text:#3a3a3a;
    --white:#ffffff;
    --canvas:#e4e4e4;
    --photo-light:#d8d8d8;
    --photo-dark:#5a5a5a;
  }
  *{box-sizing:border-box;margin:0;padding:0}
  html,body{width:857px;height:1200px;overflow:hidden}
  body{background:var(--canvas);font-family:"Questrial",sans-serif;color:var(--text);position:relative}
  .spread{position:absolute;left:38px;width:780px;height:552px;display:flex;box-shadow:0 8px 24px rgba(0,0,0,.18)}
  .spread--cover{top:24px}
  .spread--inside{top:624px}
  .page{position:relative;width:390px;height:552px;overflow:hidden;background:var(--white)}
  .page + .page{border-left:1px solid #e2e2e2}

  /* Back cover */
  .back-cover{background:var(--orange)}
  .wordmark{position:absolute;text-align:center;text-transform:uppercase;line-height:1}
  .wordmark__name{display:block;font-size:17px;letter-spacing:9px}
  .wordmark__sub{display:block;font-size:10px;letter-spacing:5px;margin-top:7px}
  .back-cover .wordmark{left:0;right:0;top:196px;color:var(--white)}
  .contact-card{position:absolute;left:100px;width:190px;top:318px;bottom:0;background:var(--white);
    display:flex;flex-direction:column;align-items:center;padding-top:22px;gap:5px;font-size:7.5px;color:var(--text);text-align:center;line-height:1.35}
  .contact-card svg{width:11px;height:11px;display:block;margin-top:4px}
  .social{display:flex;gap:5px;margin-top:10px}
  .social span{width:10px;height:10px;background:var(--black);display:block}

  /* Front cover */
  .front-cover .wordmark{left:150px;top:40px;color:var(--black)}
  .front-cover .wordmark__name{font-size:15px;letter-spacing:8px}
  .front-cover .wordmark__sub{font-size:9px}
  .photo{position:absolute;display:block}
  .photo--aqueduct-cover{left:100px;right:0;top:110px;bottom:0;
    background:linear-gradient(150deg,var(--white) 0%,var(--white) 30%,var(--photo-light) 42%,#8e8e8e 70%,var(--photo-dark) 100%)}
  .title-block{position:absolute;left:203px;width:180px;top:250px;height:165px;background:var(--orange);color:var(--white)}
  .title-block h1{font-weight:400;font-size:15px;line-height:1.2;text-transform:uppercase;padding:38px 0 0 20px}
  .title-block .url{position:absolute;right:10px;bottom:10px;font-size:7px}

  /* Inside */
  .section-title{position:absolute;left:14px;right:0;display:flex;align-items:center;gap:8px;color:var(--orange);font-size:12px;text-transform:uppercase;white-space:nowrap}
  .section-title::after{content:"";flex:1;height:4px;background:var(--orange)}
  .company .section-title{top:30px}
  .services .section-title{top:14px}
  .photo--tracks{left:0;right:0;top:52px;height:215px;
    background:linear-gradient(160deg,#9a9a9a 0%,#6e6e6e 45%,#b4b4b4 70%,#7a7a7a 100%)}
  .photo--aqueduct{left:0;right:0;top:36px;height:248px;
    background:linear-gradient(200deg,var(--photo-light) 0%,#a8a8a8 35%,var(--photo-dark) 60%,var(--white) 100%)}
  .block{position:absolute;font-size:6.8px;line-height:1.45;color:var(--text)}
  .block h2{font-weight:400;font-size:8px;color:var(--orange);text-transform:uppercase;padding-bottom:3px;margin-bottom:5px;border-bottom:1px solid var(--orange)}
  .block p + p{margin-top:4px}
  .block p + h2{margin-top:22px}
  .quote{position:absolute;left:205px;width:180px;top:370px;height:70px;background:var(--orange);color:var(--white);
    font-size:7.5px;line-height:1.4;padding:12px 12px 0 14px}
  .quote::before{content:"\201C";position:absolute;left:6px;top:2px;font-size:14px}
  .quote::after{content:"\201D";position:absolute;right:8px;bottom:2px;font-size:14px}
  .quote p + p{margin-top:6px}
</style>
</head>
<body>

<section class="spread spread--cover">
  <article class="page back-cover">
    <div class="wordmark"><span class="wordmark__name">Velbrook</span><span class="wordmark__sub">Capital</span></div>
    <address class="contact-card">
      <svg viewBox="0 0 12 12"><circle cx="6" cy="6" r="5.5" fill="none" stroke="#555"/><path d="M6 3a2 2 0 0 1 2 2c0 1.5-2 4-2 4S4 6.5 4 5a2 2 0 0 1 2-2z" fill="#555"/></svg>
      <span>Velbrook Capital SA , 14 rue<br>Lambert 75011 PARIS</span>
      <svg viewBox="0 0 12 12"><circle cx="6" cy="6" r="5.5" fill="none" stroke="#555"/><path d="M4 3.5l1 1-.6.9a4 4 0 0 0 2.2 2.2l.9-.6 1 1-.8.9C5.5 8.8 3.2 6.5 3.1 4.3z" fill="#555"/></svg>
      <span>+33 1 40 22 18 75</span>
      <svg viewBox="0 0 12 12"><circle cx="6" cy="6" r="5.5" fill="none" stroke="#555"/><circle cx="6" cy="6" r="3" fill="none" stroke="#555" stroke-width=".8"/><path d="M3 6h6M6 3v6" stroke="#555" stroke-width=".6"/></svg>
      <span>www.velbrookcapital.com</span>
      <svg viewBox="0 0 12 12"><circle cx="6" cy="6" r="5.5" fill="none" stroke="#555"/><rect x="3.3" y="4" width="5.4" height="4" fill="none" stroke="#555" stroke-width=".8"/><path d="M3.3 4l2.7 2 2.7-2" fill="none" stroke="#555" stroke-width=".8"/></svg>
      <span>contact@velbrookcapital.com</span>
      <div class="social"><span></span><span></span><span></span><span></span></div>
    </address>
  </article>

  <article class="page front-cover">
    <div class="wordmark"><span class="wordmark__name">Velbrook</span><span class="wordmark__sub">Capital</span></div>
    <div class="photo photo--aqueduct-cover" role="img" aria-label="Black and white photograph of a stone aqueduct arch against a pale sky"></div>
    <div class="title-block">
      <h1>Financial<br>Engineering</h1>
      <span class="url">www.velbrookcapital.com</span>
    </div>
  </article>
</section>

<section class="spread spread--inside">
  <article class="page company">
    <h2 class="section-title">The Company</h2>
    <div class="photo photo--tracks" role="img" aria-label="Black and white photograph of tram rails running across cobblestones"></div>
    <div class="block" style="left:20px;width:165px;top:290px">
      <h2>About us:</h2>
      <p>Velbrook Capital is a financial engineering company.</p>
      <p>It is fully independent from any bank or any other company.</p>
      <h2>What we do</h2>
      <p>We provide them with investment solutions designed to improve their portfolios performance.</p>
      <p>Simple as that.</p>
    </div>
    <div class="block" style="left:205px;width:180px;top:278px">
      <h2>Our clients:</h2>
      <p>Our clients are financial professionals such as asset managers, institutionnals, corporates, private banks, wealth managers and family offices.</p>
      <p>Our purpose is to make their work easier, every day.</p>
    </div>
    <blockquote class="quote">
      <p>Our Clients must deliver performance on their portfolio on a regular basis.</p>
      <p>We help them deliver everyday.</p>
    </blockquote>
  </article>

  <article class="page services">
    <h2 class="section-title">Our Services</h2>
    <div class="photo photo--aqueduct" role="img" aria-label="Black and white photograph of a stone aqueduct with large arches"></div>
    <div class="block" style="left:20px;width:170px;top:300px">
      <h2>Investment advice</h2>
      <p>Each client is looking for a unique investment solution. Hence, we combine internal and external resources to create the financial product that will best fit our clients requirements.</p>
      <p>Thanks to a truly independent advice, we offer bespoke,simple and efficient solutions.</p>
    </div>
    <div class="block" style="left:205px;width:175px;top:300px">
      <h2>Portfolio analysis</h2>
      <p>We advise our clients on their portfolios of financial products. Together we identify the needs for restructuring or reallocating the assets.</p>
      <p>We also provide full monitoring and reporting services throughout the life of the products.</p>
    </div>
    <div class="block" style="left:20px;width:355px;top:430px">
      <h2>Partner selection</h2>
      <p>Our internal tools allow us to continuously assess the issuers we are working with.</p>
      <p>Therefore we give our clients the luxury to chose among the best issuers for their investment solution.</p>
    </div>
  </article>
</section>

</body>
</html>
```